Epoxy Flooring Contractor business card

We need a business card to promote a new addition to our business. We now offer Epoxy Flooring. We would like for the business card to include the images attached. One is our logo, the other is a sample of metallic epoxy flooring, we would like to incorporate that somewhere into the design. I was thinking an icon of a man pushing a concrete grinder and have the color set to the metallic epoxy color. I found a business card sample on this website, I will attach it. It has the icon that we are looking for, or something similar.
Our company name is Brightmore Coatings LLC
Our owners name is Dana Pellow
Phone is 561-847-2916
website is www.brightmore-coatingsllc.com
please let me know if you need any other info

Contact Information for Business Card

Brightmore Coatings LLC
Dana Pellow, owner
Phone: 561-847-2916
Address: P.O Box 8146 Lake Worth, FL 33471
www.Brightmore-CoatingsLLC.com
BrightmoreCoatingsLLC@mailvista.net
Include logo attached
It must include a Clip art of man with concrete grinder
Must include metallic epoxy design attached
Must include the following text
Residential Garage Flooring
Epoxy Countertops
Commercial Epoxy Flooring
Restaurant Flooring
Warehouse Flooring
Licensed & Insured
Free Estimates

Colors

Designer to choose colors to be used in the design.

Requirements
Must have
• Include logo attached
• It must include a Clip art of man with concrete grinder
• Must include metallic epoxy design attached
• Must include the following text
• Garage Epoxy Flooring
• Residential Epoxy Flooring
• Concrete Floor Crack Repairs
• Concrete Floor Grinding
• Commercial & Warehouse Epoxy Flooring
• Restaurant Epoxy Flooring
• Epoxy Countertops
• Non Slip Epoxy Pool Decks
• Textured Finishes, Flakes, Granite Coat, Metallic & Quartz
• FREE ESTIMATES • LICENSED & INSURED

```html
<!DOCTYPE html>
<html lang="en">
<head>
<meta charset="utf-8">
<title>Brightmore Coatings LLC – Business Card</title>
<link rel="stylesheet" href="https://fonts.googleapis.com/css2?family=Raleway:wght@400;500;600;700&display=swap">
<style>
  :root {
    --page: #ffffff;
    --epoxy-deep: #2a5ca8;
    --epoxy-mid: #3f75c0;
    --epoxy-light: #5f92d2;
    --band: #6eaee8;
    --band-text: #4a7cc4;
    --band-strong: #5a6878;
    --frost: #eef2f6;
    --frost-2: #dfe6ee;
    --sky: #7cc0f0;
    --slate: #4f5e66;
    --white: #ffffff;
  }
  * { box-sizing: border-box; margin: 0; padding: 0; }
  html, body { width: 1000px; height: 1200px; overflow: hidden; background: var(--page); }
  body { position: relative; font-family: "Raleway", sans-serif; }

  .card { position: absolute; left: 48px; width: 902px; height: 540px; overflow: hidden; }
  .card--front { top: 38px; }
  .card--back { top: 622px; width: 900px; }

  .epoxy-texture { position: absolute; inset: 0; }
  .card--front .epoxy-texture {
    background: radial-gradient(ellipse at 30% 30%, var(--epoxy-light), transparent 60%),
                radial-gradient(ellipse at 80% 70%, var(--epoxy-mid), transparent 55%),
                var(--epoxy-deep);
  }
  .card--back .epoxy-texture {
    height: 269px;
    background: radial-gradient(ellipse at 40% 40%, var(--white), transparent 70%), var(--frost-2);
  }

  .brand { position: absolute; left: 164px; display: flex; align-items: center; gap: 14px; }
  .card--front .brand { top: 178px; }
  .card--back .brand { top: 146px; }
  .brand__mark { width: 54px; height: 54px; }
  .card--front .brand__mark { background: var(--white); }
  .card--back .brand__mark { background: var(--sky); }
  .brand__name { font-size: 34px; font-weight: 500; letter-spacing: 2px; line-height: 1.05; }
  .card--front .brand__name { color: var(--white); }
  .card--back .brand__name { color: var(--slate); }

  .grinder-figure { position: absolute; width: 190px; height: 152px; border-radius: 6px; }
  .card--front .grinder-figure { left: 548px; top: 108px; background: linear-gradient(160deg, rgba(255,255,255,.85), rgba(255,255,255,.6)); }
  .card--back .grinder-figure { left: 548px; top: 76px; background: linear-gradient(160deg, var(--slate), var(--sky)); opacity: .8; }

  .services {
    position: absolute; left: 0; top: 270px; width: 900px; height: 246px;
    background: rgba(110, 174, 232, .93);
    display: flex; flex-direction: column; align-items: center; justify-content: center; gap: 15px;
    color: var(--band-text); font-weight: 600; font-size: 21px;
  }
  .services__row { display: flex; gap: 20px; white-space: nowrap; line-height: 22px; }
  .services__row span::before { content: "•"; margin-right: 5px; }
  .services__row--strong { color: var(--band-strong); font-weight: 700; gap: 26px; }

  .accent-stripe { position: absolute; left: 0; top: 269px; width: 100%; height: 10px; background: var(--sky); }
  .contact-panel {
    position: absolute; left: 0; top: 279px; width: 100%; height: 261px;
    background: linear-gradient(135deg, var(--epoxy-mid), var(--epoxy-deep));
  }
  .owner { position: absolute; left: 48px; top: 98px; }
  .owner__company { font-size: 27px; color: var(--sky); font-weight: 500; white-space: nowrap; }
  .owner__rule { width: 222px; height: 1px; background: var(--sky); margin: 8px 0 10px; opacity: .8; }
  .owner__name { font-size: 19px; color: var(--sky); letter-spacing: 3px; }
  .divider { position: absolute; left: 406px; top: 15px; width: 2px; height: 228px; background: var(--sky); }
  .contact-list { position: absolute; left: 442px; top: 38px; list-style: none; color: var(--white); font-size: 17px; }
  .contact-list li { display: flex; align-items: flex-start; gap: 22px; line-height: 26px; margin-bottom: 16px; }
  .contact-list svg { width: 22px; height: 22px; flex: none; margin-top: 2px; fill: var(--sky); }
</style>
</head>
<body>
  <section class="card card--front">
    <div class="epoxy-texture" role="img" aria-label="Blue metallic epoxy floor texture"></div>
    <div class="brand">
      <div class="brand__mark"></div>
      <div class="brand__name">Brightmore<br>Coatings</div>
    </div>
    <div class="grinder-figure" role="img" aria-label="Silhouette of a worker pushing a concrete floor grinder"></div>
    <div class="services">
      <div class="services__row"><span>Garage Epoxy Flooring</span><span>Residential Epoxy Flooring</span><span>Restaurant Epoxy Flooring</span></div>
      <div class="services__row"><span>Concrete Floor Crack Repairs</span><span>Concrete Floor Grinding</span><span>Epoxy Countertops</span></div>
      <div class="services__row"><span>Non Slip Epoxy Pool Decks</span><span>Commercial &amp; Warehouse Epoxy Flooring</span></div>
      <div class="services__row"><span>Textured Finishes, Flakes, Granite Coat, Metallic &amp; Quartz</span></div>
      <div class="services__row services__row--strong"><span>FREE ESTIMATES</span><span>LICENSED &amp; INSURED</span></div>
    </div>
  </section>

  <section class="card card--back">
    <div class="epoxy-texture" role="img" aria-label="Pale frosted metallic epoxy texture"></div>
    <div class="brand">
      <div class="brand__mark"></div>
      <div class="brand__name">Brightmore<br>Coatings</div>
    </div>
    <div class="grinder-figure" role="img" aria-label="Worker pushing a concrete floor grinder"></div>
    <div class="accent-stripe"></div>
    <div class="contact-panel">
      <div class="owner">
        <div class="owner__company">Brightmore Coatings LLC</div>
        <div class="owner__rule"></div>
        <div class="owner__name">Dana Pellow, owner</div>
      </div>
      <div class="divider"></div>
      <ul class="contact-list">
        <li><svg viewBox="0 0 24 24"><path d="M12 2a7 7 0 0 0-7 7c0 5 7 13 7 13s7-8 7-13a7 7 0 0 0-7-7zm0 9.5A2.5 2.5 0 1 1 12 6.5a2.5 2.5 0 0 1 0 5z"/></svg><span>P.O Box 8146 Lake Worth,<br>FL 33471</span></li>
        <li><svg viewBox="0 0 24 24"><path d="M6.6 10.8a15 15 0 0 0 6.6 6.6l2.2-2.2a1 1 0 0 1 1-.25 11.4 11.4 0 0 0 3.6.57 1 1 0 0 1 1 1V20a1 1 0 0 1-1 1A17 17 0 0 1 3 4a1 1 0 0 1 1-1h3.5a1 1 0 0 1 1 1c0 1.25.2 2.45.57 3.6a1 1 0 0 1-.25 1z"/></svg><span>561-847-2916</span></li>
        <li><svg viewBox="0 0 24 24"><path d="M12 3a9 9 0 1 0 4.5 16.8l-.9-1.7A7 7 0 1 1 19 12v1a1.5 1.5 0 0 1-3 0V8h-2v.7A4.5 4.5 0 1 0 15 15.5 3.5 3.5 0 0 0 21 13v-1a9 9 0 0 0-9-9zm0 11.5a2.5 2.5 0 1 1 0-5 2.5 2.5 0 0 1 0 5z"/></svg><span>BrightmoreCoatingsLLC@mailvista.net</span></li>
        <li><svg viewBox="0 0 24 24"><path d="M12 2a10 10 0 1 0 0 20 10 10 0 0 0 0-20zm6.9 6h-2.9a15 15 0 0 0-1.4-3.6A8 8 0 0 1 18.9 8zM12 4c.8 1.2 1.5 2.5 1.9 4h-3.8c.4-1.5 1.1-2.8 1.9-4zM4.3 14a8 8 0 0 1 0-4h3.4a16 16 0 0 0 0 4zm.8 2h2.9a15 15 0 0 0 1.4 3.6A8 8 0 0 1 5.1 16zM8 8H5.1a8 8 0 0 1 4.3-3.6A15 15 0 0 0 8 8zm4 12c-.8-1.2-1.5-2.5-1.9-4h3.8c-.4 1.5-1.1 2.8-1.9 4zm2.3-6H9.7a14 14 0 0 1 0-4h4.6a14 14 0 0 1 0 4zm.3 5.6a15 15 0 0 0 1.4-3.6h2.9a8 8 0 0 1-4.3 3.6zm1.7-5.6a16 16 0 0 0 0-4h3.4a8 8 0 0 1 0 4z"/></svg><span>www.Brightmore-CoatingsLLC.com</span></li>
      </ul>
    </div>
  </section>
</body>
</html>
```